Brindle.vc needs a better website design!

We need a new and better website for Brindle.vc. We're a Canadian venture capital firm that invests in innovative entrepreneurs. We compete against the following websites: tollery.vc, quorbinvest.ca, gavelvc.com, and duskara.vc. We're a diverse group of partners and we're dedicated to the founders we invest in.
Updates

I don’t really like stock photos of random people as part of the website design…so please try to stay away from using those images. Thanks, Owen

Target Market(s)

Canadian entrepreneurs and investors

Industry/Entity Type

Venture capital, finance, investment, entrepreneurship

Coding

Coded - Design and coding required

Number of Pages Required

4 page

Font styles to use
Sans Serif

Colors

Designer to choose colors to be used in the design.

Requirements
Must have
• Clean crisp overall design. Fast and to the point.
Nice to have
• Check out www.brindle.vc - I did it myself and it is too basic and too wordy.
Should not have
• No stock images with random people in them! Not too wordy or with too many large images that are slow to load.

```html
<!DOCTYPE html>
<html lang="en">
<head>
<meta charset="utf-8">
<title>Brindle.vc — Seed-stage venture capital</title>
<link rel="stylesheet" href="https://fonts.googleapis.com/css2?family=Montserrat:wght@400;500;600;700;800&display=swap">
<style>
:root{
  --green:#7d9a2c;
  --green-light:#a8c64a;
  --ink:#1f1f1f;
  --body:#3d3d3d;
  --muted:#f4f4f4;
  --footer:#262626;
  --white:#ffffff;
}
*{box-sizing:border-box;margin:0;padding:0}
html,body{width:1200px;height:3787px;overflow:hidden}
body{font-family:'Montserrat',sans-serif;color:var(--ink);background:var(--white);position:relative}
.abs{position:absolute}
.eyebrow{color:var(--green);font-weight:600;font-size:21px;letter-spacing:.3px}
.heading{font-weight:500;font-size:38px;line-height:45px;color:var(--ink)}
.btn{position:absolute;background:var(--green);color:var(--white);font-weight:500;font-size:18px;display:flex;align-items:center;justify-content:center;letter-spacing:.3px}

/* hero */
.hero{left:0;top:0;width:1200px;height:701px;background:linear-gradient(180deg,#7d8a86 0%,#a9b3b0 35%,#8c9591 60%,#3f4a40 85%,#2a3426 100%)}
.hero-photo{position:absolute;inset:0;background:radial-gradient(ellipse at 25% 55%,rgba(40,48,45,.55),transparent 55%),radial-gradient(ellipse at 70% 30%,rgba(230,235,233,.45),transparent 50%)}
.brand{left:110px;top:15px;width:150px;text-align:center;color:var(--white)}
.brand-mark{width:92px;height:92px;border:4px solid var(--white);border-radius:50%;margin:0 auto 10px}
.brand-name{font-weight:700;font-size:24px;letter-spacing:1px}
.top-contact{right:112px;top:27px;color:var(--white);font-weight:500;font-size:17px;display:flex;align-items:center;gap:6px}
.top-contact span{color:var(--green-light)}
.nav{right:112px;top:73px;display:flex;gap:30px;color:var(--white);font-weight:500;font-size:17px}
.nav .active{color:var(--green-light)}
.hero-title{left:0;width:1200px;top:168px;text-align:center;color:var(--white);font-weight:800;font-size:88px;letter-spacing:26px;padding-left:26px}
.hero-sub{left:200px;width:800px;top:283px;text-align:center;color:var(--white);font-weight:500;font-size:25px;line-height:37px}

/* who we are */
.who-text{left:110px;top:765px;width:560px}
.who-text .heading{margin-top:22px}
.feature{position:absolute;left:110px;display:flex;align-items:center;gap:22px}
.feature-icon{width:112px;height:112px;border-radius:50%;background:#ebebeb;display:flex;align-items:center;justify-content:center}
.feature p{width:370px;font-size:18px;line-height:27px;color:var(--body)}
.who-photo{left:676px;top:783px;width:437px;height:437px;border-radius:50%;border:7px solid var(--green);background:linear-gradient(135deg,#e9e6df,#c9b79b 55%,#8c6d4c)}

/* what we fund */
.fund{left:0;top:1300px;width:1200px;height:565px;background:var(--muted);text-align:center}
.fund .eyebrow{position:absolute;left:0;width:1200px;top:73px}
.fund .heading{position:absolute;left:0;width:1200px;top:115px}
.fund-col{position:absolute;top:235px;width:300px;text-align:center}
.fund-col svg{display:block;margin:0 auto}
.fund-label{color:var(--green);font-weight:500;font-size:18px;margin-top:38px}
.fund-desc{font-size:22px;line-height:33px;margin-top:10px;font-weight:500;color:var(--ink)}

/* what we look for */
.look-frame{left:97px;top:1955px;width:403px;height:503px;border:2px solid #b8b38e}
.look-photo{left:110px;top:1943px;width:402px;height:505px;background:linear-gradient(140deg,#4d5d72,#c9ced5 45%,#e8ebee 70%,#9aa6b3)}
.look-text{left:574px;top:1940px;width:540px}
.look-text .heading{margin-top:22px}
.criteria{position:absolute;left:574px;top:2150px;display:grid;grid-template-columns:290px 260px;row-gap:17px}
.criteria li{list-style:none;display:flex;align-items:center;gap:9px;font-size:17px;color:var(--body);height:25px}

/* get in touch */
.touch{left:0;top:2535px;width:1200px;height:373px;background:linear-gradient(180deg,#9da49e 0%,#7f8a86 40%,#4d5e73 80%,#3a4d66 100%)}
.touch .eyebrow{position:absolute;left:0;width:1200px;top:60px;text-align:center;color:var(--green-light)}
.touch-heading{position:absolute;left:0;width:1200px;top:97px;text-align:center;color:var(--white);font-weight:500;font-size:36px;line-height:45px}

/* featured */
.featured .eyebrow{position:absolute;left:0;width:1200px;top:2980px;text-align:center}
.featured .heading{position:absolute;left:0;width:1200px;top:3018px;text-align:center;font-size:36px}
.logos{left:110px;top:3120px;display:grid;grid-template-columns:repeat(5,188px);grid-auto-rows:96px;gap:10px 10px}
.logo-tile{border:1px solid #dedede;display:flex;align-items:center;justify-content:center;gap:8px;font-weight:600;font-size:20px;color:#2b2b2b}
.logo-tile i{width:14px;height:14px;background:var(--green);display:inline-block}

/* footer */
.footer{left:0;top:3410px;width:1200px;height:377px;background:var(--footer);color:var(--white)}
.footer-brand{position:absolute;left:110px;top:38px;width:200px;text-align:center}
.footer-brand .brand-mark{width:145px;height:145px;border:6px solid var(--green);margin-bottom:16px}
.footer-brand .brand-name{color:var(--green);font-size:40px;letter-spacing:1px}
.footer-col{position:absolute;top:50px}
.footer-col h4{font-weight:600;font-size:17px;margin-bottom:22px}
.footer-col a{display:block;color:var(--white);text-decoration:none;font-size:16px;line-height:31px}
.footer-mail{display:flex;align-items:center;gap:10px;font-size:18px;font-weight:500}
.socials{display:flex;gap:10px;margin-top:25px}
.socials span{width:47px;height:47px;border:2px solid var(--white);border-radius:50%;display:block}
.footer-rule{position:absolute;left:110px;top:270px;width:978px;height:1px;background:#4a4a4a}
.copyright{position:absolute;left:0;width:1200px;top:303px;text-align:center;font-size:16px}
</style>
</head>
<body>

<section class="abs hero">
  <div class="hero-photo" role="img" aria-label="Misty mountain valley with evergreen forest"></div>
  <div class="abs brand"><div class="brand-mark"></div><div class="brand-name">BRINDLE.VC</div></div>
  <div class="abs top-contact">
    <svg width="16" height="12" viewBox="0 0 16 12"><rect width="16" height="12" rx="1" fill="#a8c64a"/><path d="M0 1l8 6 8-6" stroke="#7d8a86" stroke-width="1.5" fill="none"/></svg>
    Contact Us: <span>owen@brindle.vc</span>
  </div>
  <nav class="abs nav"><span class="active">HOME</span><span>TEAM</span><span>COMPANIES</span><span>WHAT WE LOOK FOR</span></nav>
  <h1 class="abs hero-title">BRINDLE</h1>
  <p class="abs hero-sub">Venture capital firm that invests in innovative seed-stage technology companies in Western Canada focused on B2B and SaaS markets.</p>
  <div class="btn" style="left:493px;top:422px;width:214px;height:68px">GET MORE INFO</div>
</section>

<section>
  <div class="abs who-text">
    <div class="eyebrow">WHO WE ARE</div>
    <h2 class="heading">We are serial entrepreneurs and venture capital investors who provide:</h2>
  </div>
  <div class="feature" style="top:980px">
    <div class="feature-icon"><svg width="56" height="56" viewBox="0 0 56 56" fill="none" stroke="#7d9a2c" stroke-width="3"><circle cx="16" cy="16" r="8"/><circle cx="16" cy="16" r="2.5" fill="#7d9a2c"/><path d="M26 16h14a8 8 0 010 16H16a8 8 0 000 16h24" stroke-dasharray="4 3"/><path d="M40 44l6 4-6 4"/></svg></div>
    <p>Mentoring and strategic advice to help you grow your company quickly and efficiently</p>
  </div>
  <div class="feature" style="top:1105px">
    <div class="feature-icon"><svg width="56" height="56" viewBox="0 0 56 56" fill="#7d9a2c"><circle cx="18" cy="14" r="8"/><path d="M4 50V36a10 10 0 0110-10h8a10 10 0 0110 10v14z"/><text x="36" y="20" font-size="18" font-family="Montserrat,sans-serif" font-weight="700">$</text><rect x="36" y="40" width="4" height="10"/><rect x="42" y="34" width="4" height="16"/><rect x="48" y="28" width="4" height="22"/></svg></div>
    <p>Investor introductions to help you raise additional follow-on funding for your startup</p>
  </div>
  <div class="abs who-photo" role="img" aria-label="Desk with laptop and printed financial charts under review"></div>
</section>

<section class="abs fund">
  <div class="eyebrow">WHAT WE FUND</div>
  <h2 class="heading">Canada's leading nationwide<br>seed stage venture fund</h2>
  <div class="fund-col" style="left:112px">
    <svg width="110" height="108" viewBox="0 0 110 108" fill="none" stroke="#8a8a8a" stroke-width="3"><rect x="8" y="40" width="94" height="56" rx="3"/><rect x="16" y="48" width="78" height="40"/><path d="M2 96h106v6H2z"/><path d="M55 4c10 8 14 22 10 40H45c-4-18 0-32 10-40z" stroke="#7d9a2c"/><circle cx="55" cy="26" r="5" stroke="#7d9a2c"/><path d="M48 50l7 10 7-10" stroke="#7d9a2c"/></svg>
    <div class="fund-label">Venture Capital Funding</div>
    <div class="fund-desc">At early-stage &amp;<br>seed stage</div>
  </div>
  <div class="fund-col" style="left:450px">
    <svg width="110" height="108" viewBox="0 0 110 108" fill="none" stroke="#8a8a8a" stroke-width="3"><circle cx="28" cy="16" r="8"/><rect x="16" y="30" width="24" height="36" rx="4"/><circle cx="80" cy="46" r="8"/><rect x="68" y="60" width="24" height="40" rx="4"/><path d="M44 12h24v14" stroke="#7d9a2c"/><path d="M62 22l6 6 6-6" stroke="#7d9a2c"/><path d="M62 94H38V80" stroke="#7d9a2c"/><path d="M32 84l6-6 6 6" stroke="#7d9a2c"/></svg>
    <div class="fund-label">$250K TO $700K</div>
    <div class="fund-desc">Various B2B and<br>SaaS sectors</div>
  </div>
  <div class="fund-col" style="left:806px">
    <svg width="110" height="108" viewBox="0 0 110 108" fill="none" stroke="#8a8a8a" stroke-width="3"><circle cx="55" cy="54" r="14" stroke="#7d9a2c"/><circle cx="55" cy="54" r="7" fill="#7d9a2c" stroke="none"/><path d="M55 4v30M55 74v30M5 34l30 12M75 62l30 12M5 74l30-12M75 46l30-12" stroke-dasharray="4 4"/></svg>
    <div class="fund-label">Sector Agnostic</div>
    <div class="fund-desc">Diversified and<br>Innovative portfolio</div>
  </div>
</section>

<section>
  <div class="abs look-frame"></div>
  <div class="abs look-photo" role="img" aria-label="Tablet and printed financial charts on a meeting table"></div>
  <div class="abs look-text">
    <div class="eyebrow">WHAT WE LOOK FOR</div>
    <h2 class="heading">We invest in innovative technology companies with these characteristics</h2>
  </div>
  <ul class="criteria">
    <li><svg width="16" height="16" viewBox="0 0 16 16"><circle cx="8" cy="8" r="8" fill="#7d9a2c"/><path d="M4.5 8.2l2.3 2.3 4.7-4.8" stroke="#fff" stroke-width="1.8" fill="none"/></svg>Founding Team</li>
    <li><svg width="16" height="16" viewBox="0 0 16 16"><circle cx="8" cy="8" r="8" fill="#7d9a2c"/><path d="M4.5 8.2l2.3 2.3 4.7-4.8" stroke="#fff" stroke-width="1.8" fill="none"/></svg>Customers</li>
    <li><svg width="16" height="16" viewBox="0 0 16 16"><circle cx="8" cy="8" r="8" fill="#7d9a2c"/><path d="M4.5 8.2l2.3 2.3 4.7-4.8" stroke="#fff" stroke-width="1.8" fill="none"/></svg>Total Addressable Market</li>
    <li><svg width="16" height="16" viewBox="0 0 16 16"><circle cx="8" cy="8" r="8" fill="#7d9a2c"/><path d="M4.5 8.2l2.3 2.3 4.7-4.8" stroke="#fff" stroke-width="1.8" fill="none"/></svg>Business Model</li>
    <li><svg width="16" height="16" viewBox="0 0 16 16"><circle cx="8" cy="8" r="8" fill="#7d9a2c"/><path d="M4.5 8.2l2.3 2.3 4.7-4.8" stroke="#fff" stroke-width="1.8" fill="none"/></svg>Product Market Fit</li>
    <li><svg width="16" height="16" viewBox="0 0 16 16"><circle cx="8" cy="8" r="8" fill="#7d9a2c"/><path d="M4.5 8.2l2.3 2.3 4.7-4.8" stroke="#fff" stroke-width="1.8" fill="none"/></svg>Competitive Advantage</li>
    <li><svg width="16" height="16" viewBox="0 0 16 16"><circle cx="8" cy="8" r="8" fill="#7d9a2c"/><path d="M4.5 8.2l2.3 2.3 4.7-4.8" stroke="#fff" stroke-width="1.8" fill="none"/></svg>Timing</li>
    <li><svg width="16" height="16" viewBox="0 0 16 16"><circle cx="8" cy="8" r="8" fill="#7d9a2c"/><path d="M4.5 8.2l2.3 2.3 4.7-4.8" stroke="#fff" stroke-width="1.8" fill="none"/></svg>Funding</li>
    <li><svg width="16" height="16" viewBox="0 0 16 16"><circle cx="8" cy="8" r="8" fill="#7d9a2c"/><path d="M4.5 8.2l2.3 2.3 4.7-4.8" stroke="#fff" stroke-width="1.8" fill="none"/></svg>Problem</li>
    <li><svg width="16" height="16" viewBox="0 0 16 16"><circle cx="8" cy="8" r="8" fill="#7d9a2c"/><path d="M4.5 8.2l2.3 2.3 4.7-4.8" stroke="#fff" stroke-width="1.8" fill="none"/></svg>Deal Terms</li>
  </ul>
  <div class="btn" style="left:574px;top:2387px;width:159px;height:59px">READ MORE</div>
</section>

<section class="abs touch" role="img" aria-label="Glass office tower seen from below against a hazy sky">
  <div class="eyebrow">GET IN TOUCH</div>
  <h2 class="touch-heading">Contact us today if you have<br>what we're looking for</h2>
  <div class="btn" style="left:520px;top:230px;width:160px;height:58px">CONTACT US</div>
</section>

<section class="featured">
  <div class="eyebrow">FEATURED COMPANIES</div>
  <h2 class="heading">Our innovative portfolio companies!</h2>
  <div class="abs logos">
    <div class="logo-tile" style="font-size:15px">TIDEWELL PULSE</div>
    <div class="logo-tile" style="font-weight:400;letter-spacing:3px;font-size:17px;color:#6a8fa0">LUMENPATH</div>
    <div class="logo-tile">Quillrun</div>
    <div class="logo-tile"><i></i>VANTOPS</div>
    <div class="logo-tile" style="font-weight:400;font-size:18px">PENNORA GO</div>
    <div class="logo-tile">Gamelyn</div>
    <div class="logo-tile" style="font-weight:400">Clearform</div>
    <div class="logo-tile" style="font-weight:400;font-size:18px">Keyvane Access</div>
    <div class="logo-tile">Nutrelab</div>
    <div class="logo-tile" style="font-weight:400;font-size:26px;color:#555">Orvane</div>
  </div>
</section>

<footer class="abs footer">
  <div class="footer-brand"><div class="brand-mark"></div><div class="brand-name">BRINDLE.VC</div></div>
  <div class="footer-col" style="left:490px">
    <h4>Quick Links</h4>
    <a href="#">Home</a><a href="#">Team</a><a href="#">Companies</a><a href="#">What We Look For</a>
  </div>
  <div class="footer-col" style="left:773px">
    <h4>Contact Us</h4>
    <div class="footer-mail"><svg width="20" height="15" viewBox="0 0 16 12"><rect width="16" height="12" rx="1" fill="#7d9a2c"/><path d="M0 1l8 6 8-6" stroke="#262626" stroke-width="1.5" fill="none"/></svg>owen@brindle.vc</div>
    <div class="socials" aria-label="Social profiles"><span></span><span></span><span></span></div>
  </div>
  <div class="footer-rule"></div>
  <p class="copyright">Copyright © 2021, Brindle. All rights reserved.</p>
</footer>

</body>
</html>
```